Wren's Hearth Support Business Card

Business card design
Font must be in Poppins Regular for Wren's Hearth Support
Safe Days Ahead font is Alex Brush

Colour must be Hex #910E2B
RGB 145-14-43
Pantone 7427 C
We want the card editable
On the front please include
Name eg Mavis Dunleavy
Position eg Clinical Care Manager
Phone number mobile 0473 856 342
Phone 08 7394 2650
Email : mavis@wrenshearthsupport.com.au
Address : Gullwing Cove, Western Australia, 6173
Website : wrenshearthsupport.com.au
Contact us today to experience the warmth, respect and personal touch of Wren's Hearth Support.

Target Market(s)

35+

Industry/Entity Type

aged care / community

Contact Information for Business Card

see project description

Requirements
Must have
• Colours, logos and fonts as detailed and uploaded

```html
<!DOCTYPE html>
<html lang="en">
<head>
<meta charset="utf-8">
<title>Wren's Hearth Support – Business Card</title>
<link rel="stylesheet" href="https://fonts.googleapis.com/css2?family=Alex+Brush&family=Poppins:wght@400;500;600&display=swap">
<style>
  :root {
    --brand-red: #910e2b;
    --brand-red-deep: #7c0b24;
    --brand-red-bright: #c8142f;
    --paper: #ffffff;
    --ink: #2b2b2b;
    --backdrop: #2a2c30;
  }
  * { box-sizing: border-box; margin: 0; padding: 0; }
  html, body {
    width: 1200px; height: 900px; overflow: hidden;
    background: var(--backdrop);
    font-family: "Poppins", sans-serif;
  }
  .sheet {
    width: 1200px; height: 900px;
    display: flex; align-items: center; justify-content: center; gap: 40px;
  }
  .card {
    position: relative;
    width: 540px; height: 330px;
    overflow: hidden;
    border-radius: 3px;
    box-shadow: 0 18px 40px rgba(0,0,0,.45);
  }

  /* ---------- front (contact side) ---------- */
  .card-front { background: var(--paper); }
  .front-swoosh { position: absolute; inset: 0; width: 100%; height: 100%; }
  .brand-block {
    position: absolute; left: 30px; top: 36px;
    display: flex; align-items: center; gap: 10px;
  }
  .brand-dot {
    width: 40px; height: 40px; border-radius: 50%;
    background: var(--brand-red); flex: none;
  }
  .brand-name {
    font-weight: 400; color: var(--brand-red);
    font-size: 19px; line-height: 1.05; letter-spacing: -.1px;
    white-space: nowrap;
  }
  .front-tagline {
    position: absolute; left: 80px; top: 88px;
    font-family: "Alex Brush", cursive;
    color: var(--brand-red); font-size: 18px;
    white-space: nowrap;
  }
  .contact-divider {
    position: absolute; left: 258px; top: 40px;
    width: 1.5px; height: 150px; background: var(--brand-red);
  }
  .contact-block {
    position: absolute; left: 272px; top: 34px; right: 12px;
    color: var(--ink); font-size: 12.5px; line-height: 1.42;
  }
  .contact-name {
    font-weight: 600; color: var(--brand-red);
    font-size: 24px; line-height: 1.1; margin-bottom: 4px;
    white-space: nowrap;
  }
  .contact-role { margin-bottom: 4px; }
  .contact-address { margin-bottom: 4px; }
  .contact-list { list-style: none; }
  .contact-list li { display: flex; align-items: center; gap: 7px; white-space: nowrap; }
  .contact-icon { width: 11px; height: 11px; flex: none; fill: var(--brand-red); }

  /* ---------- back (brand side) ---------- */
  .card-back {
    background: linear-gradient(135deg, #9a1130 0%, var(--brand-red) 55%, var(--brand-red-deep) 100%);
    color: var(--paper);
  }
  .back-emblem { position: absolute; right: -70px; bottom: -120px; width: 330px; height: 330px; }
  .back-brand { position: absolute; left: 150px; top: 44px; }
  .back-brand .brand-name { color: var(--paper); font-size: 30px; }
  .back-tagline {
    font-family: "Alex Brush", cursive;
    color: var(--paper); font-size: 21px; margin-top: 6px;
  }
  .back-message {
    position: absolute; left: 44px; top: 170px; width: 290px;
    font-size: 12px; font-weight: 600; line-height: 1.5;
  }
</style>
</head>
<body>
<main class="sheet">

  <section class="card card-front" aria-label="Business card front">
    <svg class="front-swoosh" viewBox="0 0 540 330" preserveAspectRatio="none" aria-hidden="true">
      <path d="M0 120 C 90 230, 260 300, 540 330 L 0 330 Z" fill="var(--brand-red)"/>
      <path d="M60 140 C 150 240, 300 290, 470 318" fill="none" stroke="var(--brand-red)" stroke-width="2.2"/>
    </svg>

    <div class="brand-block">
      <span class="brand-dot"></span>
      <p class="brand-name">Wren's<br>Hearth Support</p>
    </div>
    <p class="front-tagline">Safe Days Ahead</p>

    <span class="contact-divider"></span>
    <div class="contact-block">
      <p class="contact-name">Mavis Dunleavy</p>
      <p class="contact-role">Managing Director</p>
      <p class="contact-address">Gullwing Cove,<br>Western Australia, 6173</p>
      <ul class="contact-list">
        <li><svg class="contact-icon" viewBox="0 0 12 12"><rect x="3" y="0.5" width="6" height="11" rx="1.2"/></svg>0473 856 342</li>
        <li><svg class="contact-icon" viewBox="0 0 12 12"><path d="M2.5 0.8l2 .2 1 2.8-1.4 1a6 6 0 0 0 3.1 3.1l1-1.4 2.8 1 .2 2a1 1 0 0 1-1 1.1A10 10 0 0 1 1.4 1.8a1 1 0 0 1 1.1-1z"/></svg>08 7394 2650</li>
        <li><svg class="contact-icon" viewBox="0 0 12 12"><path d="M0.5 2h11v8h-11z M0.5 2l5.5 4.5L11.5 2" fill="none" stroke="var(--brand-red)" stroke-width="1.4"/></svg>mavis@wrenshearthsupport.com.au</li>
        <li><svg class="contact-icon" viewBox="0 0 12 12"><circle cx="6" cy="6" r="5" fill="none" stroke="var(--brand-red)" stroke-width="1.3"/><path d="M1 6h10M6 1c2 2.6 2 7.4 0 10M6 1c-2 2.6-2 7.4 0 10" fill="none" stroke="var(--brand-red)" stroke-width="1"/></svg>www.wrenshearthsupport.com.au</li>
      </ul>
    </div>
  </section>

  <section class="card card-back" aria-label="Business card back">
    <svg class="back-emblem" viewBox="0 0 330 330" aria-hidden="true">
      <circle cx="165" cy="165" r="158" fill="var(--brand-red-deep)" fill-opacity=".55" stroke="var(--brand-red-bright)" stroke-width="7"/>
    </svg>
    <div class="back-brand">
      <p class="brand-name">Wren's<br>Hearth Support</p>
      <p class="back-tagline">Safe Days Ahead</p>
    </div>
    <p class="back-message">Contact us today to experience the warmth, respect and personal touch of Wren's Hearth Support.</p>
  </section>

</main>
</body>
</html>
```